Wedding Invitations

We are a printing company "inkmorrow" and require multiple wedding invitation designs for our customers in store and online. We would like the designs to be editable in Photoshop if possible, if not then a layout with suggested fonts would be the next best option. We are open to suggestions on design but would like to stick to the general wedding themes some with a modern and some with a classical feel

Industry/Entity Type

Printing

```html
<!DOCTYPE html>
<html lang="en">
<head>
<meta charset="utf-8">
<title>Wedding Invitation – Victoria and David</title>
<link rel="stylesheet" href="https://fonts.googleapis.com/css2?family=Abril+Fatface&family=Josefin+Slab:wght@600&family=Oranienbaum&display=swap">
<style>
  :root {
    --paper: #fcf6c6;
    --red: #f2261a;
    --slate: #5a6264;
    --ink: #2a2a2a;
    --venue: #4f5757;
  }
  html, body {
    margin: 0;
    padding: 0;
    overflow: hidden;
    background: var(--paper);
  }
  .invitation {
    display: block;
    width: 1200px;
    height: 655px;
  }
  .card-bg { fill: var(--paper); }
  .hosts {
    font-family: "Oranienbaum", serif;
    font-size: 150px;
    fill: var(--red);
  }
  .request {
    font-family: "Oranienbaum", serif;
    font-size: 46px;
    fill: var(--slate);
  }
  .couple {
    font-family: "Oranienbaum", serif;
    font-size: 200px;
    fill: var(--slate);
  }
  .venue {
    font-family: "Josefin Slab", serif;
    font-weight: 600;
    font-size: 35px;
    fill: var(--venue);
  }
  .date-day {
    font-family: "Abril Fatface", serif;
    font-size: 74px;
    fill: var(--red);
  }
  .date-year {
    font-family: "Abril Fatface", serif;
    font-size: 78px;
    fill: var(--ink);
  }
  .sprig { fill: var(--ink); }
  .bowtie { fill: #2c2c2c; }
  .lips { fill: var(--red); }
  .band-dark { fill: var(--ink); }
  .band-red { fill: var(--red); }
</style>
</head>
<body>
<svg class="invitation" viewBox="0 0 1200 655" xmlns="http://www.w3.org/2000/svg">
  <rect class="card-bg" x="0" y="0" width="1200" height="655"/>

  <text class="hosts" x="20" y="150" textLength="1160" lengthAdjust="spacingAndGlyphs">CHARLES AND MONICA SMITH &amp; ANDREW AND CATHERINE JONES</text>

  <rect class="sprig" x="45" y="210" width="52" height="16" rx="8" role="img" aria-label="Small leaf sprig ornament"/>
  <text class="request" x="118" y="240" textLength="964" lengthAdjust="spacingAndGlyphs">Request the honor of your presence at the marriage of their children</text>
  <rect class="sprig" x="1100" y="210" width="52" height="16" rx="8" role="img" aria-label="Small leaf sprig ornament"/>

  <text class="couple" x="38" y="425" textLength="1127" lengthAdjust="spacingAndGlyphs">VICTORIA and DAVID</text>

  <rect class="bowtie" x="60" y="507" width="95" height="68" rx="14" role="img" aria-label="Black bow tie illustration"/>

  <g class="venue" text-anchor="middle">
    <text x="392" y="505">Lantern Garden in Elmwood Park</text>
    <text x="392" y="548">Riverton, New Lorne</text>
    <text x="392" y="591">Four o’clock</text>
  </g>

  <ellipse class="lips" cx="795" cy="543" rx="52" ry="32" role="img" aria-label="Red lips illustration"/>

  <text class="date-day" x="924" y="530" textLength="172" lengthAdjust="spacingAndGlyphs">14 SEP</text>
  <text class="date-year" x="922" y="600" textLength="168" lengthAdjust="spacingAndGlyphs">2014</text>

  <rect class="band-dark" x="0" y="607" width="1200" height="20"/>
  <rect class="band-red" x="0" y="627" width="1200" height="28"/>
</svg>
</body>
</html>
```